Shop window wrapping of a sports betting company

We are a sports betting company in Germany and are looking for a great outside window design for our shops.
Our 3D logo letters look like on the 4 pictures, we have sent you a shop where you can plan your design, what is important here with the shop window foiling is that it should look very modern and exclusive. we also have a website Blauhorn.com where you can take a look.

we have a premium partner a football club Falke Welkau, maybe you can integrate that but of course I'll leave that to you. The partner can be seen on the website.

I have given you a few pictures of how the current outside advertisement and the shop window at one of our locations look like at the moment. Thanks very much

Korun
Updates

Ich brauche zusätzliche Tage um durchzusehen

Target Market(s)

Sports betting

Industry/Entity Type

Ihr dürft das logo auch designen der Name BLAUHORN. Das Trikot format für das TT sollte nicht geändert werden

Requirements
Must have
• Must contain the name blue horn
Nice to have
• we have the best qoutes in all of Germany
Should not have
• Colors shouldn't evade, black red white

```html
<!DOCTYPE html>
<html lang="en">
<head>
<meta charset="utf-8">
<title>BLAUHORN – Shop Window Banners</title>
<link rel="stylesheet" href="https://fonts.googleapis.com/css2?family=Oswald:wght@400;500;700&display=swap">
<style>
  :root {
    --red: #ff1414;
    --red-deep: #d90000;
    --black: #000000;
    --ink: #0c0c0c;
    --white: #ffffff;
    --grey-light: #ebebeb;
    --grey-mid: #b9b9b9;
    --photo-dark: #1c1c1c;
    --photo-light: #8a8a8a;
  }
  * { box-sizing: border-box; margin: 0; padding: 0; }
  html, body {
    width: 1200px;
    height: 1200px;
    overflow: hidden;
  }
  body {
    position: relative;
    background: radial-gradient(ellipse at 50% 45%, var(--grey-light) 0%, #d8d8d8 55%, var(--grey-mid) 100%);
    font-family: "Oswald", "Arial Narrow", sans-serif;
    color: var(--white);
  }
  .banner {
    position: absolute;
    width: 1100px;
    height: 440px;
    background: var(--black);
    overflow: hidden;
    box-shadow: 0 26px 22px -14px rgba(0,0,0,0.55);
  }
  .banner--football { left: 30px; top: 120px; }
  .banner--tennis { left: 70px; top: 640px; }

  .banner__backdrop {
    position: absolute;
    inset: 0;
    background:
      radial-gradient(ellipse at 22% 55%, rgba(90,90,90,0.45) 0%, rgba(40,40,40,0.35) 40%, rgba(0,0,0,0) 75%),
      linear-gradient(90deg, #161616 0%, #0b0b0b 60%, #000 100%);
  }
  .banner__photo {
    position: absolute;
    top: 0;
    bottom: 0;
    right: 0;
    background: radial-gradient(ellipse at 50% 50%, var(--photo-light) 0%, #4a4a4a 40%, var(--photo-dark) 75%, var(--black) 100%);
  }
  .banner--football .banner__photo { left: 645px; }
  .banner--tennis .banner__photo { left: 690px; }

  .brand {
    position: absolute;
    left: 74px;
    top: 36px;
    width: 545px;
    height: 96px;
    background: var(--black);
    display: flex;
    align-items: center;
    justify-content: center;
  }
  .brand__name {
    font-weight: 700;
    font-size: 82px;
    letter-spacing: 2px;
    line-height: 1;
    color: var(--white);
  }
  .brand__rule {
    position: absolute;
    left: 78px;
    top: 124px;
    width: 538px;
    height: 10px;
    background: var(--red);
    box-shadow: 0 0 10px rgba(255,20,20,0.7);
  }

  .tagline {
    position: absolute;
    left: 106px;
    top: 146px;
    display: flex;
    align-items: baseline;
    gap: 12px;
    text-transform: uppercase;
    white-space: nowrap;
  }
  .tagline__lead { font-weight: 500; font-size: 28px; }
  .tagline__accent { font-weight: 700; font-size: 52px; color: var(--red); letter-spacing: 1px; }

  .offer {
    position: absolute;
    top: 218px;
    text-align: center;
  }
  .offer--fees { left: 95px; width: 200px; }
  .offer--cashback { left: 390px; width: 210px; }
  .offer__value {
    display: block;
    font-weight: 500;
    font-size: 118px;
    line-height: 1;
  }
  .offer__value .pct { color: var(--red); }
  .offer__label {
    display: block;
    margin-top: 2px;
    font-weight: 700;
    font-size: 36px;
    line-height: 1.1;
    text-transform: uppercase;
    white-space: nowrap;
  }
  .offer__label .dollar { color: var(--red); }
  .offer-join {
    position: absolute;
    left: 310px;
    top: 248px;
    font-weight: 500;
    font-size: 70px;
    line-height: 1;
  }

  .notice {
    position: absolute;
    left: 0;
    top: 389px;
    width: 638px;
    height: 51px;
    background: var(--red-deep);
    background: linear-gradient(90deg, var(--red) 0%, var(--red-deep) 100%);
    clip-path: polygon(0 0, 100% 0, 96% 100%, 0 100%);
    display: flex;
    align-items: center;
    padding-left: 26px;
    font-weight: 400;
    font-size: 24px;
    letter-spacing: 1.5px;
    text-transform: uppercase;
    white-space: nowrap;
  }
  .notice strong { font-weight: 700; margin: 0 0.3em; }
  .notice .gap { margin-left: 0.4em; }
</style>
</head>
<body>

  <section class="banner banner--football">
    <div class="banner__backdrop" role="img" aria-label="Faint black and white crowd of cheering fans"></div>
    <div class="banner__photo" role="img" aria-label="Black and white photo of two football players fighting for the ball, one sliding into a tackle"></div>

    <div class="brand"><span class="brand__name">BLAUHORN</span></div>
    <div class="brand__rule"></div>

    <p class="tagline"><span class="tagline__lead">Win with the</span><span class="tagline__accent">King of odds</span></p>

    <p class="offer offer--fees"><span class="offer__value">0<span class="pct">%</span></span><span class="offer__label">Betting fees</span></p>
    <span class="offer-join">&amp;</span>
    <p class="offer offer--cashback"><span class="offer__value">20<span class="pct">%</span></span><span class="offer__label">Ca<span class="dollar">$</span>hback</span></p>

    <p class="notice">Cashback <span class="gap">is credited</span><strong>21st</strong>day of every<strong>month</strong></p>
  </section>

  <section class="banner banner--tennis">
    <div class="banner__backdrop" role="img" aria-label="Faint black and white crowd of cheering fans"></div>
    <div class="banner__photo" role="img" aria-label="Black and white photo of a tennis player swinging a racket at the ball"></div>

    <div class="brand"><span class="brand__name">BLAUHORN</span></div>
    <div class="brand__rule"></div>

    <p class="tagline"><span class="tagline__lead">Win with the</span><span class="tagline__accent">King of odds</span></p>

    <p class="offer offer--fees"><span class="offer__value">0<span class="pct">%</span></span><span class="offer__label">Betting fees</span></p>
    <span class="offer-join">&amp;</span>
    <p class="offer offer--cashback"><span class="offer__value">20<span class="pct">%</span></span><span class="offer__label">Ca<span class="dollar">$</span>hback</span></p>

    <p class="notice">Cashback <span class="gap">is credited</span><strong>21st</strong>day of every<strong>month</strong></p>
  </section>

</body>
</html>
```